Gospel Tract titled "Steps Along the Lantern Road."

This will be a bi-fold brochure. The design will be in the front panel of the brochure which is 4 inches wide and 8.5 inches high. This is a common brochure among Gospel tracts in the series, "Steps along the lantern road near ______________ ." The blank is usually a state, city, or other location. I want a "fun" image of Iowa or something representing Iowa at the bottom. A graphic representing "heaven" at the top. Perhaps a meandering road between the two. The words, "Steps Along the Lantern Road", but be on the front somewhere. I am also open to other designs with this theme and the words "Steps Along the Lantern Road." My suggestion is just one idea.

Non-Christians who are interested in knowing how to get to heaven

• Something specific to the state of Iowa at the bottom: farms, state fair, cows, barns, power windmills, the capitol building, etc.
• I would like something bright, colorful, with a fun Iowa image at the bottom.
• Religous symbolism....no doves, angels, crosses, etc.

```html
<!DOCTYPE html>
<html lang="en">
<head>
<meta charset="utf-8">
<title>Steps Along the Lantern Road</title>
<link rel="stylesheet" href="https://fonts.googleapis.com/css2?family=Anton&family=Bebas+Neue&family=Allura&display=swap">
<style>
  :root {
    --sky-top: #35c6ee;
    --sky-glow: #f4f1ff;
    --cloud-pink: #e7a9d6;
    --cloud-lavender: #a995dc;
    --sky-low: #4f8fd9;
    --horizon-blue: #6c9fd8;
    --sunset: #f49a3c;
    --field-green: #3f8f2e;
    --field-dark: #2c5f22;
    --kicker-red: #8a1530;
    --kicker-olive: #7f8a2c;
    --kicker-ink: #1c1050;
    --title-navy: #1f2f9a;
    --title-ice: #9ff1ff;
    --title-white: #ffffff;
  }
  * { margin: 0; padding: 0; box-sizing: border-box; }
  html, body { width: 1200px; height: 2548px; overflow: hidden; background: #ffffff; }
  .cover { position: relative; width: 1200px; height: 2548px; overflow: hidden; }

  .sky-art {
    position: absolute; left: 0; top: 0; width: 1200px; height: 2150px;
    background:
      radial-gradient(ellipse 320px 260px at 600px 470px, var(--sky-glow) 0%, rgba(255,240,250,0.6) 35%, rgba(255,255,255,0) 100%),
      linear-gradient(180deg, var(--sky-top) 0%, #7fc3ef 12%, var(--cloud-pink) 26%, var(--cloud-lavender) 42%, #8f9be0 58%, var(--sky-low) 72%, var(--horizon-blue) 86%, #c9a9b8 94%, var(--sunset) 100%);
  }
  .farm-art {
    position: absolute; left: 0; top: 2150px; width: 1200px; height: 398px;
    background: linear-gradient(180deg, var(--field-dark) 0%, var(--field-green) 40%, #4c9a36 70%, var(--field-dark) 100%);
  }
  .title { position: absolute; left: 0; top: 0; width: 1200px; height: 2548px; }
  .kicker { font-family: 'Bebas Neue', 'Oswald', sans-serif; }
  .headline { font-family: 'Anton', 'Oswald', sans-serif; }
  .script { font-family: 'Allura', cursive; }
</style>
</head>
<body>
<main class="cover">
  <div class="sky-art" role="img" aria-label="Painted heavenly sky with radiant sun, pink and lavender clouds and a long stairway rising toward the light"></div>
  <div class="farm-art" role="img" aria-label="Photo of a rural gravel road beside green fields and an old weathered barn at sunset"></div>

  <svg class="title" viewBox="0 0 1200 2548">
    <defs>
      <linearGradient id="kickerFill" x1="0" y1="0" x2="1" y2="0">
        <stop offset="0" stop-color="var(--kicker-ink)"/>
        <stop offset="0.4" stop-color="var(--kicker-olive)"/>
        <stop offset="0.7" stop-color="var(--kicker-red)"/>
        <stop offset="1" stop-color="var(--kicker-red)"/>
      </linearGradient>
      <linearGradient id="iceFill" x1="0" y1="0" x2="1" y2="1">
        <stop offset="0" stop-color="var(--title-white)"/>
        <stop offset="0.45" stop-color="var(--title-ice)"/>
        <stop offset="1" stop-color="var(--title-white)"/>
      </linearGradient>
    </defs>
    <text class="kicker" x="345" y="597" textLength="525" lengthAdjust="spacingAndGlyphs"
          font-size="120" fill="url(#kickerFill)">STEPS ALONG</text>
    <text class="headline" x="58" y="985" textLength="1088" lengthAdjust="spacingAndGlyphs"
          font-size="385" fill="var(--title-navy)" fill-opacity="0.78">LANTERN</text>
    <text class="headline" x="85" y="1714" textLength="1050" lengthAdjust="spacingAndGlyphs"
          font-size="575" fill="url(#iceFill)" fill-opacity="0.88">ROAD</text>
    <text class="script" x="330" y="1115" textLength="560" lengthAdjust="spacingAndGlyphs"
          font-size="360" fill="var(--title-white)">the</text>
  </svg>
</main>
</body>
</html>
```